Stationery including letterhead, business cards, for a new Chartered Accounting Practice

I need a new set of stationery including letterhead, business cards, for a new Chartered Accounting Practice based in Melbourne, Victoria, Australia called "Brint Holloway, Chartered Accountant".

I will be providing Auditing and general consulting advice to small and medium business enterprises. The final design should communicate trust, wisdom and security.

Target Market(s)

Target Market English speaking, Australians. Proprietors small and medium sized businesses - aged 45-65. Fellow professionals - lawyers, investment consultants, other accountants. Retirees - aged 60 and over

Industry/Entity Type

Accountant

Font styles to use
Serif

Colors
0355a3

Requirements
Must have
• The final design should convey trust, wisdom and security.
• Names of practice "Brint Holloway , Chartered Accountant"
• Contact details:
• Address 284 Marbury Street, Tallow Creek, Victoria, 3172, Australia
• Telephone: 047 000 3158
• Email: brintholloway@postquill.example
Nice to have
• an expensive and professional design, the letterhead should be timeless with a logo on white space
Should not have
• no bright/fluro colours

```html
<!DOCTYPE html>
<html lang="en">
<head>
<meta charset="utf-8">
<title>Brint Holloway, Chartered Accountant — Business Cards</title>
<link rel="stylesheet" href="https://fonts.googleapis.com/css2?family=Cinzel:wght@500;600&family=Questrial&family=Open+Sans:wght@400&display=swap">
<style>
  :root {
    --brand-blue: #0355a3;
    --band-dark: #252525;
    --card-white: #ffffff;
    --card-back: #f7f7f7;
    --ink-grey: #4a4a4a;
    --stage: #e9e9ea;
  }
  * { box-sizing: border-box; margin: 0; padding: 0; }
  html, body { width: 1200px; height: 900px; overflow: hidden; }
  body { background: var(--stage); position: relative; font-family: "Open Sans", sans-serif; }

  .card { position: absolute; box-shadow: 0 6px 18px rgba(0,0,0,0.18); overflow: hidden; }
  .card--front { left: 178px; top: 74px; width: 588px; height: 364px; background: var(--card-white); }
  .card--back { left: 388px; top: 505px; width: 566px; height: 352px; background: var(--card-back); }

  .card__bands { position: absolute; inset: 0; }

  .wordmark { position: absolute; left: 0; right: 0; text-align: center; }
  .wordmark__name {
    font-family: "Cinzel", serif; font-weight: 600; color: var(--brand-blue);
    font-size: 38px; letter-spacing: 0.5px; line-height: 1;
  }
  .wordmark__title {
    font-family: "Questrial", sans-serif; color: var(--ink-grey);
    font-size: 14px; letter-spacing: 5.4px; margin-top: 6px; line-height: 1;
  }
  .card--front .wordmark { top: 66px; left: 8px; }
  .card--back .wordmark { top: 196px; }

  .contact { position: absolute; color: #fff; font-size: 15px; line-height: 21px; }
  .contact--direct { left: 34px; top: 282px; }
  .contact--direct li { list-style: none; display: flex; align-items: center; gap: 5px; }
  .contact--direct svg { width: 13px; height: 13px; fill: #fff; }
  .contact--address { right: 38px; top: 264px; text-align: right; font-style: normal; }

  .mark { position: absolute; left: 0; right: 0; top: 108px; display: flex; justify-content: center; align-items: center; gap: 12px; }
  .mark__square { width: 22px; height: 22px; background: var(--brand-blue); }
  .mark__name { font-family: "Cinzel", serif; font-weight: 600; color: var(--brand-blue); font-size: 46px; line-height: 1; }
</style>
</head>
<body>

  <section class="card card--front" aria-label="Business card front">
    <svg class="card__bands" viewBox="0 0 588 364" aria-hidden="true">
      <polygon points="0,188 405,188 379,214 0,214" fill="var(--band-dark)"/>
      <polygon points="0,219 384,219 419,181 588,181 588,364 0,364" fill="var(--brand-blue)"/>
    </svg>
    <div class="wordmark">
      <div class="wordmark__name">BRINT HOLLOWAY</div>
      <div class="wordmark__title">CHARTERED ACCOUNTANT</div>
    </div>
    <ul class="contact contact--direct">
      <li><svg viewBox="0 0 24 24"><path d="M6.6 10.8a15.1 15.1 0 0 0 6.6 6.6l2.2-2.2c.3-.3.7-.4 1-.2 1.1.4 2.3.6 3.6.6.6 0 1 .4 1 1V20c0 .6-.4 1-1 1A17 17 0 0 1 3 4c0-.6.4-1 1-1h3.5c.6 0 1 .4 1 1 0 1.3.2 2.5.6 3.6.1.3 0 .7-.2 1z"/></svg>047 000 3158</li>
      <li><svg viewBox="0 0 24 24"><path d="M2 5h20v14H2zm2 2v.5l8 5 8-5V7l-8 5z"/></svg>brintholloway@postquill.example</li>
    </ul>
    <address class="contact contact--address">
      284 Marbury Street,<br>
      Tallow Creek, Victoria,<br>
      3172, Australia
    </address>
  </section>

  <section class="card card--back" aria-label="Business card back">
    <div class="mark">
      <span class="mark__square" aria-hidden="true"></span>
      <span class="mark__name">Holloway</span>
    </div>
    <div class="wordmark">
      <div class="wordmark__name">BRINT HOLLOWAY</div>
      <div class="wordmark__title">CHARTERED ACCOUNTANT</div>
    </div>
  </section>

</body>
</html>
```